Flyer design

We need a marketing flyer to use when meeting with clients. We may also use it for mailings. Please see the attached document and images. Not all images need to be used. Please feel free to edit / photoshop images. Please also see our website : www.kelvorantissue.com

Industry/Entity Type

Marketing

```html
<!DOCTYPE html>
<html lang="en">
<head>
<meta charset="utf-8">
<title>Kelvoran Dermatology &amp; Dermatopathology – Flyer</title>
<link href="https://fonts.googleapis.com/css2?family=Questrial&family=Libre+Baskerville:wght@400;700&display=swap" rel="stylesheet">
<style>
  :root {
    --page-bg: #e9e6e1;
    --tissue-deep: #8e1b35;
    --tissue-mid: #b8465c;
    --tissue-light: #d98a92;
    --panel: #f1f1f2;
    --panel-edge: #dcdcde;
    --ink: #2b2b2e;
    --ink-soft: #4a4a4f;
    --accent-red: #d0202a;
    --white: #ffffff;
  }
  * { box-sizing: border-box; margin: 0; padding: 0; }
  html, body { width: 1200px; height: 1000px; overflow: hidden; background: var(--page-bg); }
  body { font-family: "Questrial", sans-serif; color: var(--ink); }

  .flyer {
    position: absolute; left: 280px; top: 45px;
    width: 640px; height: 910px;
    background: var(--panel);
    box-shadow: 0 10px 30px rgba(0,0,0,.25);
    overflow: hidden;
  }
  .tissue-header {
    position: absolute; left: 0; top: 0; width: 100%; height: 250px;
    background: radial-gradient(ellipse at 35% 60%, var(--tissue-light), var(--tissue-mid) 45%, var(--tissue-deep) 100%);
  }
  .tissue-footer {
    position: absolute; left: 0; bottom: 0; width: 100%; height: 210px;
    background: radial-gradient(ellipse at 60% 30%, var(--tissue-light), var(--tissue-mid) 40%, var(--tissue-deep) 100%);
  }
  .content-panel {
    position: absolute; left: 0; top: 220px; width: 100%; height: 490px;
    background: linear-gradient(180deg, var(--white), var(--panel) 60%, var(--panel-edge));
  }

  .brand {
    position: absolute; right: 34px; top: 70px;
    display: flex; align-items: center; gap: 12px;
  }
  .brand-dot { width: 22px; height: 22px; border-radius: 50%; background: var(--accent-red); }
  .brand-name {
    font-size: 17px; letter-spacing: .5px; color: var(--ink); line-height: 1.25; text-align: right;
    text-transform: uppercase;
  }

  .copy { position: absolute; left: 36px; top: 246px; width: 350px; font-size: 13.5px; line-height: 1.35; color: var(--ink-soft); }
  .copy p { margin-bottom: 12px; }
  .copy .services { font-weight: 700; color: var(--ink); margin-bottom: 12px; }
  .copy .services li { list-style: none; }
  .web-link { color: var(--accent-red); font-weight: 700; font-size: 17px; margin: 4px 0 16px; }
  .since { font-weight: 700; color: var(--ink); margin-bottom: 6px !important; }

  .gallery { position: absolute; right: 30px; top: 248px; display: flex; flex-direction: column; gap: 14px; }
  .gallery-frame {
    width: 200px; height: 138px; border: 6px solid var(--white);
    box-shadow: 0 3px 8px rgba(0,0,0,.3);
  }
  .gallery-frame.microscope { background: linear-gradient(135deg, #3c3c40, #8a8a90 55%, #2a2a2e); }
  .gallery-frame.slide-low { background: radial-gradient(circle, #e8dfb0 55%, #1e1e1e 72%); }
  .gallery-frame.slide-high { background: radial-gradient(circle, #d47c86 50%, #a53a4d 66%, #1e1e1e 72%); }

  .doctor-photo {
    position: absolute; left: 34px; top: 640px; width: 160px; height: 120px;
    border: 6px solid var(--white); background: linear-gradient(160deg, #c9c1a5, #8a8672 55%, #2e3340);
    box-shadow: 0 3px 8px rgba(0,0,0,.3);
  }
  .doctor-name {
    position: absolute; left: 36px; top: 778px;
    font-family: "Libre Baskerville", serif; font-weight: 700; font-size: 24px; color: var(--white);
  }
  .doctor-credentials {
    position: absolute; left: 36px; top: 814px;
    font-family: "Libre Baskerville", serif; font-size: 12px; color: var(--white); opacity: .9;
  }
</style>
</head>
<body>
  <main class="flyer">
    <div class="tissue-header" role="img" aria-label="Magnified pink skin tissue sample background"></div>
    <div class="content-panel"></div>
    <div class="tissue-footer" role="img" aria-label="Magnified pink skin tissue sample background"></div>

    <div class="brand">
      <span class="brand-dot"></span>
      <span class="brand-name">Kelvoran<br>Dermatology &amp; Dermatopathology</span>
    </div>

    <section class="copy">
      <p>Commitment to helping find solutions, either in-house or through our contacts, for all your dermatopathology needs, including but not limited to:</p>
      <p>Dermatopathology consultative service – First or second opinions, off-site or on-site.</p>
      <ul class="services">
        <li>Tissue processing</li>
        <li>Mohs technicians</li>
        <li>Immunohistochemistry and special stains</li>
      </ul>
      <p class="web-link">www.kelvorantissue.com</p>
      <p class="since">Practicing Dermatopathology since 2007.</p>
      <p>Access to an extensive range of special and immunohistochemistry stains, and patient-centered consideration of the judicious use of them.</p>
      <p>Usually 2-3 day turnaround time depending on the circumstance of the case.</p>
      <p>Courier pick up can usually be arranged.</p>
    </section>

    <div class="gallery">
      <div class="gallery-frame microscope" role="img" aria-label="Microscope lens over a glass slide"></div>
      <div class="gallery-frame slide-low" role="img" aria-label="Low-power microscope view of a tissue section"></div>
      <div class="gallery-frame slide-high" role="img" aria-label="High-power microscope view of stained tissue"></div>
    </div>

    <div class="doctor-photo" role="img" aria-label="Portrait photo of the physician"></div>
    <h2 class="doctor-name">Dana R. Holm, M.D.</h2>
    <p class="doctor-credentials">Board Certified – Dermatopathology • Board Certified – Dermatology</p>
  </main>
</body>
</html>
```